Healing stone/crystal Shopify store

Hi - I'm creating a new site to sell healing crystals/stones.Name for the shop is MoonpetalHaven. Site helps people to choose best crystals for them .Shop should have blog aswell.The site should be informative and attractive. Stones we sell Opalite,Green Aventurine,Watermelon Crystal,Rose Quartz Stone,Tiger Eye Stone. Must be Shopify. No content yet, you can fill neccessary fields Lorea Ipsum and if you have some good idea you can put it there
Updates

Designs look the same

Target Market(s)

Woman, English speaking countries.

Industry/Entity Type

Shop

Number of Pages Required

1 page

Colors

Designer to choose colors to be used in the design.

Requirements
Must have
• Blog
Nice to have
• High quality pictures to look site attractive.

```html
<!DOCTYPE html>
<html lang="en">
<head>
<meta charset="utf-8">
<title>MoonpetalHaven – Healing Stones & Crystals</title>
<link rel="stylesheet" href="https://fonts.googleapis.com/css2?family=Merriweather:wght@400;700;900&family=Roboto:wght@500;700&display=swap">
<style>
:root{
  --plum:#7e2a6b;
  --plum-line:#a45a96;
  --mint:#86d97a;
  --mint-dark:#5fbf52;
  --blush:#f1e5ee;
  --ink:#2b2b2b;
  --paper:#ffffff;
}
*{box-sizing:border-box;margin:0;padding:0}
html,body{width:714px;height:1200px;overflow:hidden;background:var(--paper)}
body{position:relative;font-family:'Merriweather',Georgia,serif;color:var(--ink)}
.abs{position:absolute}

/* header */
.site-header{position:absolute;left:0;top:0;width:714px;height:52px;background:var(--plum);border-radius:0 0 6px 6px}
.brand{left:96px;top:9px;color:#fff}
.brand-name{font-size:15px;font-weight:700;color:var(--mint);letter-spacing:.2px}
.brand-tag{font-size:8px;color:#fff;margin-top:3px}
.search{left:254px;top:19px;width:130px;height:15px;background:#fff;border:2px solid var(--mint);border-radius:3px;font-size:7px;color:#aaa;padding:1px 6px}
.search-btn{left:370px;top:19px;width:14px;height:15px;background:var(--mint);border-radius:0 3px 3px 0}
.main-nav{left:442px;top:5px;display:flex;gap:12px;font-size:7.5px;color:#fff}
.main-nav .active{color:var(--mint)}
.social{top:27px;width:13px;height:13px;border-radius:50%;background:#fff;opacity:.9}
.cart-sum{left:572px;top:25px;font-size:6.5px;font-weight:700;color:#fff;text-align:center;line-height:9px}

/* stones row */
.stone-nav{top:58px;left:0;width:714px;height:24px}
.stone-link{position:absolute;top:0;display:flex;align-items:center;gap:6px;font-size:7px;font-weight:700}
.thumb{width:24px;height:20px;border-radius:40% 50% 40% 45%}
.rule{left:96px;top:90px;width:522px;height:1px;background:#d8ecd3}

/* hero */
.card{position:absolute;background:#fff;border:2px solid var(--mint);border-radius:3px;box-shadow:0 0 4px rgba(0,0,0,.08)}
.card-side{top:167px;width:126px;height:96px}
.card-side .photo{position:absolute;left:8px;top:24px;width:40px;height:48px;border-radius:40%}
.card-side .copy{position:absolute;left:56px;top:28px;width:66px;text-align:center;font-size:5.5px;font-weight:700;line-height:9px}
.accent{color:var(--mint)}
.btn-ghost{display:block;margin:5px auto 0;width:58px;height:18px;border:1.5px solid var(--mint);border-radius:2px;font-size:5.5px;line-height:15px;letter-spacing:.5px}
.card-main{left:237px;top:112px;width:242px;height:181px}
.card-main .photo{position:absolute;left:10px;top:18px;width:110px;height:148px;border-radius:45% 45% 20% 20%;background:radial-gradient(ellipse at 50% 40%,#f6f8f3,#cfd8d6 60%,#b9bdb0)}
.card-main .copy{position:absolute;left:118px;top:60px;width:118px;text-align:center;font-size:9.5px;font-weight:700;line-height:17px}
.btn-solid{display:block;margin:7px auto 0;width:106px;height:21px;background:var(--mint);color:#fff;border-radius:2px;font-size:7px;letter-spacing:.8px;line-height:21px}
.dot{top:300px;width:7px;height:7px;border:1.2px solid var(--mint);border-radius:50%}

/* mission */
.mission-band{left:0;top:318px;width:714px;height:300px}
.mission-title{left:0;top:352px;width:714px;text-align:center;font-size:14px;font-weight:700}
.mission-title em,.adv-title em{font-style:normal;color:var(--plum)}
.mission-sub{left:0;top:371px;width:714px;text-align:center;font-size:11px;font-weight:700}
.mission-text{left:193px;width:320px;font-size:6.3px;line-height:10.8px;color:#333}
.adv-title{left:0;top:495px;width:714px;text-align:center;font-size:14px;font-weight:700}
.adv{top:522px;display:flex;align-items:center;gap:8px;font-size:7px;font-weight:700}

/* products */
.product{position:absolute;width:142px}
.product-frame{width:142px;height:99px;border:2.5px solid var(--plum-line);border-radius:2px;padding:4px}
.product-frame div{width:100%;height:100%}
.product-name{margin-top:8px;text-align:center;font-size:7px;line-height:10px;height:22px}
.price-row{position:relative;height:22px;margin-top:4px}
.price{position:absolute;left:0;bottom:0;font-size:11px;font-weight:700;color:var(--plum)}
.old{position:absolute;left:16px;top:-2px;font-size:5.5px;text-decoration:line-through;color:#333}
.buy{position:absolute;right:0;top:0;width:65px;height:21px;background:var(--plum);color:#fff;font-family:'Roboto',Arial,sans-serif;font-weight:700;font-size:7.5px;text-align:center;line-height:21px;border-radius:2px}
.buy.hot{background:var(--mint)}

/* footer */
.site-footer{left:0;top:990px;width:714px;height:210px}
.foot-links{left:0;top:1013px;width:714px;display:flex;justify-content:center;gap:17px;font-size:7px;font-weight:700;color:#fff}
.map{left:182px;top:1053px;width:176px;height:101px;border-radius:2px;background:linear-gradient(135deg,#eef0ec,#e2e6df 60%,#f0ede2)}
.contact-title{left:394px;top:1039px;font-size:7px;font-weight:700;color:#fff}
.field{left:394px;width:136px;background:#fff;border-radius:2px;font-size:6.5px;color:#777;padding:5px 7px}
.submit{left:466px;top:1163px;width:64px;height:21px;background:#fff;border:1.5px solid var(--plum);border-radius:3px;font-size:7px;font-weight:700;text-align:center;line-height:18px}
</style>
</head>
<body>

<header class="site-header">
  <div class="abs brand">
    <div class="brand-name">MoonpetalHaven</div>
    <div class="brand-tag">Healing Stones<span class="accent">&amp;</span>Crystals</div>
  </div>
  <div class="abs search">search</div>
  <div class="abs search-btn">
    <svg width="14" height="15" viewBox="0 0 14 15"><circle cx="6.5" cy="6.5" r="3" fill="none" stroke="#fff" stroke-width="1.3"/><line x1="8.7" y1="8.7" x2="11" y2="11" stroke="#fff" stroke-width="1.3"/></svg>
  </div>
  <nav class="abs main-nav"><span>Home</span><span>Need Help?</span><span class="active">Blog</span><span>Contact</span><span>Log In</span></nav>
  <span class="abs social" style="left:472px"></span>
  <span class="abs social" style="left:493px"></span>
  <span class="abs social" style="left:514px"></span>
  <svg class="abs" style="left:547px;top:24px" width="20" height="18" viewBox="0 0 20 18">
    <path d="M6 7 Q10 0 14 7" fill="none" stroke="var(--mint)" stroke-width="1.6"/>
    <path d="M2 7 H18 L16 17 H4 Z" fill="var(--mint)"/>
  </svg>
  <div class="abs cart-sum">200 $<br>3</div>
</header>

<nav class="abs stone-nav">
  <div class="stone-link" style="left:103px"><div class="thumb" role="img" aria-label="Opalite elephant figurine" style="background:#cbd3d8"></div>Opalite</div>
  <div class="stone-link" style="left:176px"><div class="thumb" role="img" aria-label="Green Aventurine elephant figurine" style="background:#9cc1a6"></div>Green Aventurine</div>
  <div class="stone-link" style="left:288px"><div class="thumb" role="img" aria-label="Watermelon Crystal elephant figurine" style="background:#e0707a"></div>Watermelon Crystal</div>
  <div class="stone-link" style="left:407px"><div class="thumb" role="img" aria-label="Rose Quartz elephant figurine" style="background:#d9a3bd"></div>Rose Quartz Stone</div>
  <div class="stone-link" style="left:522px"><div class="thumb" role="img" aria-label="Tiger Eye elephant figurine" style="background:#8a5a36"></div>Tiger Eye Stone</div>
</nav>
<div class="abs rule"></div>

<section class="hero">
  <div class="card card-side" style="left:96px">
    <div class="photo" role="img" aria-label="Green Aventurine elephant figurine" style="background:#9cc1a6"></div>
    <div class="copy">Support Your Heart<br>With <span class="accent">Green Aventurine</span><span class="btn-ghost">SEE MORE</span></div>
  </div>
  <div class="card card-main">
    <div class="photo" role="img" aria-label="Opalite angel figurine"></div>
    <div class="copy">Boost Your Self-Esteem<br>With <span class="accent">Opalite</span><span class="btn-solid">SEE MORE</span></div>
  </div>
  <div class="card card-side" style="left:492px">
    <div class="photo" role="img" aria-label="Tiger Eye angel figurine" style="background:linear-gradient(#9a6a3a,#5e3b22)"></div>
    <div class="copy">Increase Your Luck<br>With <span class="accent">Tiger Eye</span> Stone<span class="btn-ghost">SEE MORE</span></div>
  </div>
  <span class="abs dot" style="left:338px;background:var(--mint);box-shadow:inset 0 0 0 1.5px #fff"></span>
  <span class="abs dot" style="left:347px"></span>
  <span class="abs dot" style="left:356px"></span>
</section>

<section>
  <svg class="abs mission-band" width="714" height="300" viewBox="0 0 714 300">
    <path d="M0 10 C120 2 240 14 360 8 C480 2 600 14 714 6 V276 Q680 274 640 284 Q600 296 560 282 Q520 268 480 272 Q440 276 400 286 Q360 294 320 280 Q280 266 240 276 Q200 288 160 290 Q120 292 80 278 Q40 270 0 274 Z" fill="var(--blush)"/>
    <path d="M0 10 C120 2 240 14 360 8 C480 2 600 14 714 6" fill="none" stroke="var(--plum-line)" stroke-width="1"/>
    <path d="M0 274 Q40 270 80 278 Q120 292 160 290 Q200 288 240 276 Q280 266 320 280 Q360 294 400 286 Q440 276 480 272 Q520 268 560 282 Q600 296 640 284 Q680 274 714 276" fill="none" stroke="var(--plum-line)" stroke-width="1.2"/>
  </svg>
  <h2 class="abs mission-title">Our <em>Mission</em></h2>
  <p class="abs mission-sub">Heal with crystals <span class="accent">&amp;</span> stones</p>
  <p class="abs mission-text" style="top:391px">Lorem ipsum dolor sit amet, consectetur adipisicing elit, sed do eiusmod tempor incididunt ut labore et dolore magna aliqua. Ut enim ad minim veniam, quis nostrud exercitation ullamco laboris nisi ut aliquip ex ea commodo consequat. Duis aute irure dolor in reprehenderit in voluptate velit esse cillum dolore eu fugiat nulla pariatur.</p>
  <p class="abs mission-text" style="top:442px">Excepteur sint occaecat cupidatat non proident, sunt in culpa qui officia deserunt mollit anim id est laborum. Sed ut perspiciatis unde omnis iste natus error sit voluptatem accusantium doloremque laudantium, totam rem aperiam, eaque ipsa quae ab illo inventore veritatis et quasi architecto beatae vitae dicta sunt explicabo.</p>
  <h2 class="abs adv-title">Our <em>Advantages</em></h2>
  <div class="abs adv" style="left:156px">
    <svg width="26" height="30" viewBox="0 0 26 30" fill="none" stroke="#222" stroke-width="1.2"><circle cx="13" cy="11" r="9"/><circle cx="13" cy="11" r="6"/><path d="M13 7 L14.2 10 L17 10 L14.8 12 L15.6 15 L13 13.3 L10.4 15 L11.2 12 L9 10 L11.8 10 Z"/><path d="M7 18 L4 28 L8 26 L10 29 L12 20 M19 18 L22 28 L18 26 L16 29 L14 20"/></svg>
    High-Quality Goods
  </div>
  <div class="abs adv" style="left:301px">
    <svg width="30" height="30" viewBox="0 0 30 30" fill="none" stroke="#222" stroke-width="1.2"><circle cx="20" cy="5" r="3.5"/><path d="M5 16 Q5 9 15 9 Q25 9 25 17 Q25 23 19 25 V28 H16 V26 H12 V28 H9 V25 Q4 23 4 19 H2 V15 H5"/><circle cx="9" cy="15" r=".8" fill="#222"/></svg>
    Good Prices
  </div>
  <div class="abs adv" style="left:438px">
    <svg width="44" height="28" viewBox="0 0 44 28" fill="none" stroke="#222" stroke-width="1.2"><path d="M1 6 L8 3 L14 17 L7 20 Z M43 6 L36 3 L30 17 L37 20 Z"/><path d="M11 8 L17 6 Q20 5 24 7 L30 8 M13 16 L19 23 Q21 25 23 23 L31 15 M24 7 L19 12 Q21 14 24 11 L29 14"/></svg>
    Competent Support
  </div>
</section>

<section class="products">
  <article class="product" style="left:116px;top:632px">
    <div class="product-frame"><div role="img" aria-label="Watermelon Crystal elephant figurine" style="background:radial-gradient(ellipse at 50% 55%,#e9707c,#f4c3c6 70%,#fff)"></div></div>
    <h3 class="product-name">Watermelon Crystal<br>“Elephant”</h3>
    <div class="price-row"><span class="old">30$</span><span class="price">10$</span><span class="buy">BUY</span></div>
  </article>
  <article class="product" style="left:285px;top:632px">
    <div class="product-frame"><div role="img" aria-label="Green Aventurine angel figurine" style="background:radial-gradient(ellipse at 50% 50%,#8fc3a0,#d4eadb 65%,#fff)"></div></div>
    <h3 class="product-name">Green Aventurine Angel</h3>
    <div class="price-row"><span class="old">300$</span><span class="price">200$</span><span class="buy hot">BUY</span></div>
  </article>
  <article class="product" style="left:454px;top:632px">
    <div class="product-frame"><div role="img" aria-label="Circle of amethyst angel figurines" style="background:radial-gradient(circle at 50% 50%,#fff 10%,#7a5e86 35%,#d7cfdc 65%,#fff)"></div></div>
    <h3 class="product-name">Rose Quartz Stone Complect</h3>
    <div class="price-row"><span class="old">500$</span><span class="price">300$</span><span class="buy">BUY</span></div>
  </article>

  <article class="product" style="left:116px;top:821px">
    <div class="product-frame"><div role="img" aria-label="Dark pyrite angel figurine" style="background:radial-gradient(ellipse at 50% 50%,#4a4636,#b9b6ab 60%,#fff)"></div></div>
    <h3 class="product-name">Tiger Eye Stone Anglel</h3>
    <div class="price-row"><span class="old">1000$</span><span class="price">800$</span><span class="buy">BUY</span></div>
  </article>
  <article class="product" style="left:285px;top:821px">
    <div class="product-frame"><div role="img" aria-label="Three Rose Quartz angel figurines" style="background:radial-gradient(ellipse at 50% 50%,#eeafb8,#f8dde1 65%,#fff)"></div></div>
    <h3 class="product-name">Rose Quartz Stone (3 items)</h3>
    <div class="price-row"><span class="old">200$</span><span class="price">150$</span><span class="buy">BUY</span></div>
  </article>
  <article class="product" style="left:454px;top:821px">
    <div class="product-frame"><div role="img" aria-label="Group of sodalite angel figurines" style="background:radial-gradient(ellipse at 50% 50%,#2f3468,#b2b4cc 65%,#fff)"></div></div>
    <h3 class="product-name">Opalite (4 items)</h3>
    <div class="price-row"><span class="old">1500$</span><span class="price">1000$</span><span class="buy">BUY</span></div>
  </article>
</section>

<footer>
  <svg class="abs site-footer" width="714" height="210" viewBox="0 0 714 210">
    <path d="M0 8 C180 0 360 14 540 6 C620 3 680 5 714 8 V210 H0 Z" fill="var(--mint)"/>
  </svg>
  <nav class="abs foot-links"><span>Opalite</span><span>Green Aventurine</span><span>Watermelon Crystal</span><span>Rose Quartz Stone</span><span>Tiger Eye Stone</span></nav>
  <div class="abs map" role="img" aria-label="Map showing the shop location"></div>
  <svg class="abs" style="left:253px;top:1122px" width="12" height="16" viewBox="0 0 12 16"><path d="M6 15 Q1 8 1 5.5 A5 5 0 0 1 11 5.5 Q11 8 6 15 Z" fill="#e0453a"/><circle cx="6" cy="5.5" r="1.8" fill="#fff"/></svg>
  <div class="abs contact-title">Contact Us</div>
  <div class="abs field" style="top:1054px;height:17px">Your Name</div>
  <div class="abs field" style="top:1080px;height:18px">Your Email</div>
  <div class="abs field" style="top:1107px;height:48px">Your Message</div>
  <div class="abs submit">SUBMIT</div>
</footer>

</body>
</html>
```